Buch-/eBook-Cover für ein Verona PQN Taschenbuch
Zielgruppe
Tau & Linde Verlag ist ein moderner Verlag für islamische Bücher über innere Heilung, Herzruhe und persönliche Entwicklung im Licht des Qurans und der Sunnah. Der Verlag verbindet spirituelle Tiefe mit emotionalen Alltagsthemen wie Overthinking, Angst, Sabr, Tawakkul, Selbstheilung und innerem Frieden.
Aufgabenstellung
Wir benötigen ein modernes! Cover für ein Verona PQN Taschenbuch in deutscher Sprache.
Titel: Oh Himmel, meine Sorgen ziehen weiter
Untertitel: Wie du durch die Sunnah Ruhe findest - auch wenn deine Gedanken dich nicht loslassen
Autorenname: Leyla Doruk
Verlagsname: Tau & Linde Verlag
Nische: Islam + Overthinking
Zielgruppe: Islamische Frauen
Vermarktung: Über ClipWave
Es soll ein emotional ansprechendes Cover erstellt werden im modernen Design in deutscher Sprache für die Zielgruppe islamische Frauen.
Cover für Verona PQN
Maße:
15,24 x 22,86 cm
6 x 9 Zoll
Vorder und Rückseite
Das Design darf nicht zu überladen sein.

```html
<!DOCTYPE html>
<html lang="de">
<head>
<meta charset="utf-8">
<title>Oh Himmel – Buchcover</title>
<link rel="stylesheet" href="https://fonts.googleapis.com/css2?family=Sofia&family=Open+Sans:wght@400;700&display=swap">
<style>
  :root {
    --page-bg: #e8e8e8;
    --sky-top: #0a1440;
    --sky-mid: #152a6e;
    --sky-low: #2a4a8e;
    --text-light: #ffffff;
    --text-cream: #fff8e6;
    --outline-dark: #0b1030;
  }
  html, body {
    margin: 0;
    padding: 0;
    width: 967px;
    height: 1200px;
    overflow: hidden;
    background: var(--page-bg);
  }
  .canvas {
    position: relative;
    width: 967px;
    height: 1200px;
  }
  .cover {
    position: absolute;
    left: 123px;
    top: 60px;
    width: 722px;
    height: 1080px;
    overflow: hidden;
    color: var(--text-light);
    font-family: "Open Sans", Arial, sans-serif;
    text-align: center;
  }
  .cover-art {
    position: absolute;
    inset: 0;
    background:
      radial-gradient(circle at 50% 17%, rgba(190,225,255,0.55) 0 70px, rgba(120,170,230,0.15) 110px, transparent 170px),
      radial-gradient(ellipse at 50% 95%, rgba(140,170,220,0.55) 0, rgba(90,120,190,0.25) 220px, transparent 420px),
      linear-gradient(180deg, var(--sky-top) 0%, var(--sky-mid) 55%, var(--sky-low) 100%);
  }
  .author {
    position: absolute;
    top: 26px;
    left: 0;
    right: 0;
    font-family: "Sofia", cursive;
    font-size: 24px;
    color: var(--text-light);
  }
  .title {
    position: absolute;
    top: 318px;
    left: 0;
    right: 0;
    margin: 0;
    font-family: "Sofia", cursive;
    font-weight: 400;
    font-size: 96px;
    line-height: 1.1;
    color: var(--text-light);
    text-shadow:
      0 0 3px var(--outline-dark), 2px 2px 0 var(--outline-dark), -2px -2px 0 var(--outline-dark),
      2px -2px 0 var(--outline-dark), -2px 2px 0 var(--outline-dark), 0 0 14px rgba(255,255,255,0.35);
  }
  .title-line2 {
    position: absolute;
    top: 486px;
    left: 0;
    right: 0;
    margin: 0;
    font-size: 31px;
    font-weight: 400;
    color: var(--text-light);
    text-shadow: 0 0 4px #000, 1px 1px 2px #000;
  }
  .subtitle {
    position: absolute;
    top: 584px;
    left: 0;
    right: 0;
    margin: 0;
    font-size: 19px;
    line-height: 1.2;
    color: var(--text-cream);
    text-shadow: 0 0 3px #000, 1px 1px 2px #000;
  }
  .publisher {
    position: absolute;
    bottom: 26px;
    left: 0;
    right: 0;
    font-size: 18px;
    line-height: 1.5;
    text-shadow: 0 0 4px #000;
  }
  .publisher-name {
    display: block;
    font-weight: 700;
    font-size: 20px;
  }
</style>
</head>
<body>
<div class="canvas">
  <div class="cover">
    <div class="cover-art" role="img" aria-label="Nachthimmel mit Sternen und Mondsichel, unten zum Gebet geöffnete Hände"></div>
    <div class="author">Leyla Doruk</div>
    <h1 class="title">Oh Himmel</h1>
    <p class="title-line2">Meine Sorgen Ziehen Weiter</p>
    <p class="subtitle">Wie du durch die Sunnah Ruhe findest -<br>auch wenn deine Gedanken dich nicht loslassen</p>
    <div class="publisher">
      Verlagsname:
      <span class="publisher-name">Tau &amp; Linde Verlag</span>
    </div>
  </div>
</div>
</body>
</html>
```